A new website for Electrical Contractor Business

We are looking for a unique and new WordPress website design which would include 5 Pages - Home Page, Meet the Team, Our Services, Our Projects and Contact Us page.

The global theme for the website needs to be professional but simple to navigate as we cater for both business and home owner customers.

Our core business service is targeted around lighting from single room decorative to large office so the theme should incorporate this in some way.

The home page should include;
Our business logo, Contact number, Email address, small Image rotation box - Highlighting pervious projectsText box - With welcome message, twitter feed news reel/Customer feed back box.

I would also like to see a 2 boxes for the separate customer types we services. Business and Home Owner. each box will have a small image with a small text description with a link to the area of the services page relevant to that customer type.

Meet the team page -This will be introducing potential customers to the team so I would like it to include for each team member. Something like a small image and text area which will introduce an outline of the team members skills and abilities.

Our Services page This page will be outlining the different services on offer to the both customer types business and homeowner. Each service should have an image with text description of the service would good here.

Our projects page-Will include images of pervious projects and work we have completed along with a text area for the project description/ outliner.

Contact Us page - Should include a contact form which should include an option for the customer to quest us to call them back, also a selection box for them to inform us our how they found our details would be good.

Colour - The theme colours can be taken from the logo or feel free to impress with your own imagination.

Remember we are looking for a website that will interest our customers enough to except our services or be drawn further into the website.. So call to action links to other areas of the site/ contact page are welcome

Target Market(s)

Business - Office, warehousing and Large Store - lighting and Power
Home owner lighting and power

Coding

Coded - Design and coding required

Number of Pages Required

5+ page

Font styles to use
Serif
Sans Serif

Colors

Designer to choose colors to be used in the design.

Requirements
Must have
• Logo integrated into the website design - i.e. website colours which allow the logo to blend into the design.
Nice to have
• Custom but professional theme catering to business customers, but also show that we do provide services to home owners too.
Should not have
• Sorry am not interested in one oversized block image on rotation covering half the home page.. Images will be needed but not a single block over sized frame with not text, shape. Please use your imagination when considering this design

```html
<!DOCTYPE html>
<html lang="en">
<head>
<meta charset="utf-8">
<title>Voltcrest Lighting</title>
<link rel="stylesheet" href="https://fonts.googleapis.com/css2?family=Montserrat:wght@400;500;600;700;800&display=swap">
<style>
:root{
  --navy:#1f3466;
  --navy-dark:#182a55;
  --orange:#f26a2a;
  --text:#555b66;
  --light:#f4f4f4;
  --white:#ffffff;
  --border:#c9ccd3;
}
*{box-sizing:border-box;margin:0;padding:0}
html,body{width:1200px;height:3210px;overflow:hidden}
body{font-family:"Montserrat",sans-serif;color:var(--text);background:var(--white);position:relative}
.abs{position:absolute}
/* top bar */
.topbar{position:absolute;left:0;top:0;width:1200px;height:95px;border-top:3px solid var(--navy);background:var(--white)}
.brand{position:absolute;left:77px;top:27px;display:flex;align-items:center;gap:12px}
.brand-dot{width:44px;height:44px;border-radius:50%;background:var(--orange)}
.brand-name{font-weight:700;font-size:19px;color:var(--navy);letter-spacing:1px}
.top-contact{position:absolute;top:22px;display:flex;align-items:center;gap:14px}
.top-icon{width:48px;height:48px;border:2px solid var(--orange);border-radius:50%;display:flex;align-items:center;justify-content:center}
.top-label{font-size:13px;color:#666;letter-spacing:.5px}
.top-value{font-size:17px;color:#444;margin-top:4px}
/* nav */
.nav{position:absolute;left:0;top:95px;width:1200px;height:53px;background:var(--orange)}
.nav a{position:absolute;top:0;height:53px;line-height:53px;font-size:13.5px;color:var(--white);text-decoration:none;letter-spacing:.3px}
.nav .active{background:var(--navy);padding:0 20px;left:77px}
.nav .cta{left:956px;width:167px;text-align:center;background:var(--navy);font-weight:700;font-size:15px}
/* hero */
.hero{position:absolute;left:0;top:148px;width:1200px;height:552px;overflow:hidden}
.hero-photo{position:absolute;inset:0;background:linear-gradient(90deg,#7a5a26 0%,#b98a3c 30%,#6e6a55 45%,#3c4f7c 60%,#2d3f6c 100%)}
.hero-tint{position:absolute;inset:0}
.hero h1{position:absolute;left:659px;top:152px;font-size:38px;line-height:44px;font-weight:700;color:var(--white);letter-spacing:1px}
.hero p{position:absolute;left:659px;top:275px;width:460px;font-size:18px;line-height:31px;color:var(--white)}
.hero-strip{position:absolute;left:323px;top:670px;width:554px;height:62px}
.strip-text{position:absolute;top:670px;height:62px;line-height:62px;font-size:15px;color:var(--white);display:flex;align-items:center;gap:14px}
/* welcome */
.welcome-title{position:absolute;left:79px;top:803px;font-size:34px;line-height:48px;font-weight:800;color:var(--navy);letter-spacing:.5px}
.welcome-title span{color:var(--orange)}
.copy{font-size:13px;line-height:25px;color:var(--text)}
.welcome-intro{position:absolute;left:79px;top:922px;width:615px}
.welcome-more{position:absolute;left:329px;top:1027px;width:365px}
.welcome-mark{position:absolute;left:77px;top:1027px;width:188px;height:182px;display:flex;align-items:center;justify-content:center}
.quote{position:absolute;left:769px;top:807px;width:354px;height:396px;border:1px solid var(--border);border-radius:4px;background:var(--white)}
.quote-field{position:absolute;left:27px;width:300px;border:1px solid var(--border);background:#f7f7f7;font-size:13px;color:#777;padding:12px 16px}
.quote-send{position:absolute;left:27px;top:318px;width:300px;height:42px;background:var(--navy);color:var(--white);font-weight:700;font-size:18px;text-align:center;line-height:42px;letter-spacing:.5px}
/* services */
.services{position:absolute;left:0;top:1283px;width:1200px;height:437px}
.svc{position:absolute;top:0;width:600px;height:437px;text-align:center;color:var(--white)}
.svc-home{left:0;background:linear-gradient(135deg,#2a3e72,#1c2d5a)}
.svc-office{left:600px;background:linear-gradient(135deg,#f07a3a,#e9692b)}
.svc-icon{position:absolute;left:248px;top:48px;width:132px;height:132px;border-radius:50%;border:4px solid var(--white);display:flex;align-items:center;justify-content:center}
.svc h3{position:absolute;left:0;width:600px;top:190px;font-size:23px;font-weight:700}
.svc p{position:absolute;left:80px;width:450px;top:230px;font-size:13px;line-height:25px}
.svc-plus{position:absolute;left:279px;top:344px;width:40px;height:40px;border-radius:50%;background:var(--white);display:flex;align-items:center;justify-content:center}
/* gallery */
.section-title{position:absolute;left:0;width:1200px;text-align:center;font-size:34px;font-weight:800;color:var(--navy);letter-spacing:.5px}
.section-title span{color:var(--orange)}
.tile{position:absolute;width:239px;height:166px}
/* testimonials */
.testimonials{position:absolute;left:0;top:2303px;width:1200px;height:501px;background:var(--light)}
.card{position:absolute;top:121px;width:323px;height:301px;background:var(--white);padding:23px 22px}
.card p{font-size:13px;line-height:25px}
.card-foot{position:absolute;left:22px;top:250px;display:flex;align-items:center;gap:16px;font-size:12.5px;font-weight:600;color:var(--navy)}
.stars{display:flex;gap:3px}
/* footer */
.footer{position:absolute;left:0;top:2804px;width:1200px;height:346px;background:var(--navy)}
.footer .brand{left:77px;top:52px}
.footer .brand-name{color:var(--white)}
.footer-about{position:absolute;left:79px;top:150px;width:290px;font-size:13px;line-height:25px;color:var(--white)}
.footer h4{position:absolute;top:70px;font-size:18px;font-weight:700;color:var(--orange);letter-spacing:.5px}
.f-item{position:absolute;display:flex;gap:16px;font-size:13px;line-height:25px;color:var(--white)}
.f-item small{display:block;color:var(--orange);font-size:12.5px;margin-top:6px}
.bottombar{position:absolute;left:0;top:3150px;width:1200px;height:60px;background:var(--orange);text-align:center;line-height:60px;font-size:13px;color:var(--white)}
</style>
</head>
<body>

<svg width="0" height="0" style="position:absolute">
  <defs>
    <path id="star" d="M9 0l2.6 6 6.4.5-4.9 4.2 1.5 6.3L9 13.6 3.4 17l1.5-6.3L0 6.5 6.4 6z"/>
  </defs>
</svg>

<header class="topbar">
  <div class="brand"><div class="brand-dot"></div><div class="brand-name">VOLTCREST LIGHTING</div></div>
  <div class="top-contact" style="left:611px">
    <div class="top-icon"><svg width="18" height="14" viewBox="0 0 18 14"><rect width="18" height="14" rx="2" fill="#1f3466"/><path d="M1 2l8 6 8-6" stroke="#fff" stroke-width="1.6" fill="none"/></svg></div>
    <div><div class="top-label">EMAIL US ON</div><div class="top-value">info@voltcrest-lighting.com</div></div>
  </div>
  <div class="top-contact" style="left:917px">
    <div class="top-icon"><svg width="18" height="18" viewBox="0 0 24 24"><path fill="#1f3466" d="M6.6 10.8a15.1 15.1 0 006.6 6.6l2.2-2.2a1 1 0 011-.25 11.4 11.4 0 003.6.6 1 1 0 011 1V20a1 1 0 01-1 1A17 17 0 013 4a1 1 0 011-1h3.5a1 1 0 011 1c0 1.25.2 2.45.6 3.6a1 1 0 01-.25 1z"/></svg></div>
    <div><div class="top-label">CALL US ON</div><div class="top-value">123 456 7890</div></div>
  </div>
</header>

<nav class="nav">
  <a class="active" href="#">HOME</a>
  <a href="#" style="left:187px">MEET THE TEAM</a>
  <a href="#" style="left:353px">OUR SERVICES</a>
  <a href="#" style="left:503px">PROJECTS</a>
  <a href="#" style="left:626px">CONTACT</a>
  <a class="cta" href="#">GET IN TOUCH</a>
</nav>

<section class="hero">
  <div class="hero-photo" role="img" aria-label="Photo of a modern office reception with pendant lighting and a lobby"></div>
  <svg class="hero-tint" width="1200" height="552"><polygon points="640,0 1200,0 1200,552 485,552" fill="#1f3466" opacity=".72"/></svg>
  <h1>LOREM IPSUM IS<br>SIMPLY DUMMY TEXT</h1>
  <p>Lorem Ipsum is dummy text of the printing and typesetting industry. Lorem Ipsum has been the industry's standard dummy text ever.</p>
</section>
<svg class="hero-strip" width="554" height="62" viewBox="0 0 554 62">
  <polygon points="30,0 242,0 242,62 30,62 0,31" fill="#f26a2a"/>
  <polygon points="242,0 524,0 554,31 524,62 242,62" fill="#1f3466"/>
</svg>
<div class="strip-text" style="left:378px"><svg width="20" height="20" viewBox="0 0 24 24"><path fill="#fff" d="M6.6 10.8a15.1 15.1 0 006.6 6.6l2.2-2.2a1 1 0 011-.25 11.4 11.4 0 003.6.6 1 1 0 011 1V20a1 1 0 01-1 1A17 17 0 013 4a1 1 0 011-1h3.5a1 1 0 011 1c0 1.25.2 2.45.6 3.6a1 1 0 01-.25 1z"/></svg>123 456 7890</div>
<div class="strip-text" style="left:604px"><svg width="18" height="14" viewBox="0 0 18 14"><rect width="18" height="14" rx="2" fill="#fff"/><path d="M1 2l8 6 8-6" stroke="#1f3466" stroke-width="1.6" fill="none"/></svg>info@voltcrest-lighting.com</div>

<section>
  <h2 class="welcome-title"><span>WELCOME TO</span> VOLTCREST<br>LIGHTING</h2>
  <p class="copy welcome-intro">Lorem Ipsum is simply dummy text of the printing and typesetting industry. Lorem Ipsum has been the industry's standard dummy text ever since the 1500s, when an unknown printer took a galley of type and scrambled it to make a type specimen book.</p>
  <div class="welcome-mark"><div style="width:170px;height:170px;border-radius:50%;border:12px solid var(--navy)"></div></div>
  <p class="copy welcome-more">It has survived not only five centuries, but also the leap into electronic typesetting, remaining essentially unchanged. It was popularised in the 1960s with the release of Letraset sheets containing Lorem Ipsum passages, and more recently with desktop publishing software like Aldus PageMaker including versions of Lorem Ipsum.</p>

  <div class="quote">
    <svg class="abs" style="left:-1px;top:-1px" width="354" height="84"><polygon points="0,0 354,0 354,64 177,84 0,64" fill="#1f3466"/></svg>
    <div class="abs" style="left:0;top:22px;width:354px;text-align:center;color:#fff;font-weight:700;font-size:21px;letter-spacing:.5px">GET FREE QUOTE</div>
    <div class="quote-field" style="top:110px;height:42px">Name</div>
    <div class="quote-field" style="top:162px;height:42px">Email</div>
    <div class="quote-field" style="top:215px;height:93px">Message</div>
    <div class="quote-send">SEND</div>
  </div>
</section>

<section class="services">
  <div class="svc svc-home" role="img" aria-label="Photo of a living room with decorative lighting under a navy tint">
    <div class="svc-icon" style="background:var(--orange)"><svg width="64" height="60" viewBox="0 0 64 60"><path d="M32 4L4 30h8v26h15V40h10v16h15V30h8z" fill="#fff"/></svg></div>
    <h3>Room decorative lighting</h3>
    <p>Lorem Ipsum is simply dummy text of the printing and typesetting industry. Lorem Ipsum has been the industry's standard dummy text ever since the 1500s, when an unknown printer took a galley of type and scrambled it to make a type specimen book.</p>
    <div class="svc-plus"><svg width="20" height="20"><path d="M10 2v16M2 10h16" stroke="#1f3466" stroke-width="2"/></svg></div>
  </div>
  <div class="svc svc-office" role="img" aria-label="Photo of an open plan office under an orange tint">
    <div class="svc-icon" style="left:220px;background:var(--navy)"><svg width="56" height="60" viewBox="0 0 56 60"><rect x="16" y="4" width="24" height="26" rx="6" fill="#fff"/><rect x="6" y="22" width="6" height="14" rx="3" fill="#fff"/><rect x="44" y="22" width="6" height="14" rx="3" fill="#fff"/><rect x="12" y="32" width="32" height="6" rx="3" fill="#fff"/><path d="M28 38v10M14 54l14-6 14 6" stroke="#fff" stroke-width="4" fill="none"/></svg></div>
    <h3>Office decorative lighting</h3>
    <p style="left:70px">Lorem Ipsum is simply dummy text of the printing and typesetting industry. Lorem Ipsum has been the industry's standard dummy text ever since the 1500s, when an unknown printer took a galley of type and scrambled it to make a type specimen book.</p>
    <div class="svc-plus" style="left:267px"><svg width="20" height="20"><path d="M10 2v16M2 10h16" stroke="#1f3466" stroke-width="2"/></svg></div>
  </div>
</section>

<section>
  <h2 class="section-title" style="top:1790px"><span>PROJECT</span> GALLERY</h2>
  <div class="tile" style="left:77px;top:1859px;background:linear-gradient(135deg,#3a3430,#cfc6bb)" role="img" aria-label="Project photo: lounge with sofas"></div>
  <div class="tile" style="left:346px;top:1859px;background:linear-gradient(135deg,#5a4a44,#c9b8ac)" role="img" aria-label="Project photo: dining room with pendant lamps"></div>
  <div class="tile" style="left:616px;top:1859px;background:linear-gradient(135deg,#6b4a34,#d8d0c6)" role="img" aria-label="Project photo: hotel bedroom"></div>
  <div class="tile" style="left:883px;top:1859px;background:linear-gradient(135deg,#e6e6e8,#9a8a78)" role="img" aria-label="Project photo: office with ceiling lighting"></div>
  <div class="tile" style="left:77px;top:2057px;background:linear-gradient(135deg,#ece8e4,#b9b2aa)" role="img" aria-label="Project photo: bright living room"></div>
  <div class="tile" style="left:346px;top:2057px;background:linear-gradient(135deg,#8b6a4a,#4a3426)" role="img" aria-label="Project photo: open hallway with stairs"></div>
  <div class="tile" style="left:616px;top:2057px;background:linear-gradient(135deg,#d9d6d2,#5e4a3a)" role="img" aria-label="Project photo: reception desk with round ceiling"></div>
  <div class="tile" style="left:883px;top:2057px;background:linear-gradient(135deg,#3a2416,#d9903e)" role="img" aria-label="Project photo: warmly lit bedroom"></div>
</section>

<section class="testimonials">
  <h2 class="section-title" style="top:50px"><span>CLIENT</span> TESTIMONIALS</h2>
  <div class="card" style="left:77px"><p>Lorem Ipsum is simply dummy text of the printing and typesetting industry. Lorem Ipsum has been the industry's standard dummy text ever since the 1500s, when an unknown printer took a galley of type and scrambled it to make a type specimen book. It has survived not only five centurie but also the leap into electronic.</p>
    <div class="card-foot">– NAME SURNAME<div class="stars"><svg width="105" height="18" viewBox="0 0 105 18"><g fill="#f26a2a"><use href="#star"/><use href="#star" x="21"/><use href="#star" x="42"/><use href="#star" x="63"/><use href="#star" x="84"/></g></svg></div></div></div>
  <div class="card" style="left:438px"><p>Lorem Ipsum is simply dummy text of the printing and typesetting industry. Lorem Ipsum has been the industry's standard dummy text ever since the 1500s, when an unknown printer took a galley of type and scrambled it to make a type specimen book.</p>
    <div class="card-foot">– NAME SURNAME<div class="stars"><svg width="105" height="18" viewBox="0 0 105 18"><g fill="#f26a2a"><use href="#star"/><use href="#star" x="21"/><use href="#star" x="42"/><use href="#star" x="63"/><use href="#star" x="84"/></g></svg></div></div></div>
  <div class="card" style="left:800px"><p>Lorem Ipsum is simply dummy text of the printing and typesetting industry. Lorem Ipsum has been the industry's standard dummy text ever since the 1500s, when an unknown printer took a galley of type and scrambled it to make a type specimen book. It has survived not only five centurie but also the leap into electronic.</p>
    <div class="card-foot">– NAME SURNAME<div class="stars"><svg width="105" height="18" viewBox="0 0 105 18"><g fill="#f26a2a"><use href="#star"/><use href="#star" x="21"/><use href="#star" x="42"/><use href="#star" x="63"/><use href="#star" x="84"/></g></svg></div></div></div>
</section>

<footer class="footer">
  <div class="brand"><div class="brand-dot" style="background:#fff"></div><div class="brand-name">VOLTCREST LIGHTING</div></div>
  <p class="footer-about">Lorem Ipsum is simply dummy text of the printing and typesetting industry. Lorem Ipsum has been the industry's standard.</p>

  <h4 style="left:441px">RECENT TWEETS</h4>
  <div class="f-item" style="left:441px;top:106px"><svg width="28" height="26" viewBox="0 0 28 26"><path d="M4 2h20a3 3 0 013 3v11a3 3 0 01-3 3H12l-6 5v-5H4a3 3 0 01-3-3V5a3 3 0 013-3z" fill="#fff"/></svg><div>Lorem Ipsum is simply dummy text of<br>the printing and typesetting industry.<small>4 days ago</small></div></div>
  <div class="f-item" style="left:441px;top:205px"><svg width="28" height="26" viewBox="0 0 28 26"><path d="M4 2h20a3 3 0 013 3v11a3 3 0 01-3 3H12l-6 5v-5H4a3 3 0 01-3-3V5a3 3 0 013-3z" fill="#fff"/></svg><div>Lorem Ipsum is simply dummy text of<br>the printing and typesetting industry.<small>4 days ago</small></div></div>

  <h4 style="left:802px">CONTACT INFO</h4>
  <div class="f-item" style="left:800px;top:106px"><svg width="20" height="24" viewBox="0 0 20 24"><path d="M10 0a8 8 0 00-8 8c0 6 8 15 8 15s8-9 8-15a8 8 0 00-8-8zm0 11a3 3 0 110-6 3 3 0 010 6z" fill="#f26a2a"/></svg><div>Lorem Ipsum is simply dummy text of<br>the printing and typesetting industry.</div></div>
  <div class="f-item" style="left:800px;top:170px"><svg width="20" height="20" viewBox="0 0 24 24"><path fill="#f26a2a" d="M6.6 10.8a15.1 15.1 0 006.6 6.6l2.2-2.2a1 1 0 011-.25 11.4 11.4 0 003.6.6 1 1 0 011 1V20a1 1 0 01-1 1A17 17 0 013 4a1 1 0 011-1h3.5a1 1 0 011 1c0 1.25.2 2.45.6 3.6a1 1 0 01-.25 1z"/></svg><div>123 456 7890</div></div>
  <div class="f-item" style="left:800px;top:208px"><svg width="20" height="16" viewBox="0 0 18 14"><rect width="18" height="14" rx="2" fill="#f26a2a"/><path d="M1 2l8 6 8-6" stroke="#1f3466" stroke-width="1.6" fill="none"/></svg><div>info@voltcrest-lighting.com</div></div>
</footer>
<div class="bottombar">©VOLTCREST LIGHTING - 2019. All Rights Reserved.</div>

</body>
</html>
```